Painting Company Business Card

Brightwell Painting needs a new business card. See attachments for our logo and current card as an example.
We want to utilize the same colors in the logo, and keep all the information that is currently on it. Just need an updated and modern design.
We are open to loosing the Association Logos if it means a better design.
We are also entertaining a spot for a picture of a headshot of the person listed on the card. Head shot can be finished later.

```html
<!DOCTYPE html>
<html lang="en">
<head>
<meta charset="utf-8">
<title>Brightwell Painting – Business Card</title>
<link href="https://fonts.googleapis.com/css2?family=Lato:wght@400;700;900&display=swap" rel="stylesheet">
<style>
  :root {
    --olive: #3c4530;
    --maroon: #6b3a36;
    --white: #ffffff;
    --paper: #fdfdfb;
    --stage: #e9e9e6;
    --photo-top: #dfe6ec;
    --photo-bottom: #b9c7d4;
  }
  * { margin: 0; padding: 0; box-sizing: border-box; }
  html, body { width: 1200px; height: 895px; overflow: hidden; }
  body {
    background: var(--stage);
    font-family: "Lato", sans-serif;
    display: flex;
    flex-direction: column;
    align-items: center;
    justify-content: center;
    gap: 36px;
  }
  .card {
    position: relative;
    width: 660px;
    height: 380px;
    overflow: hidden;
    box-shadow: 0 6px 18px rgba(0,0,0,.18);
  }
  .wordmark {
    position: absolute;
    top: 34px;
    right: 44px;
    width: 250px;
    font-weight: 900;
    font-size: 40px;
    line-height: 1.02;
    letter-spacing: .5px;
    text-transform: uppercase;
    text-align: left;
  }
  /* back side */
  .card-back { background: var(--olive); color: var(--white); }
  .card-back .wordmark { color: var(--white); }
  .contact-list {
    position: absolute;
    left: 44px;
    bottom: 44px;
    padding-left: 16px;
    border-left: 2px solid var(--white);
    list-style: none;
    font-size: 15px;
    line-height: 1.55;
  }
  .contact-list li { display: flex; align-items: center; gap: 10px; }
  .contact-list svg { width: 12px; height: 12px; fill: none; stroke: var(--white); stroke-width: 1.6; }
  /* front side */
  .card-front { background: var(--paper); }
  .card-front .wordmark { color: var(--olive); }
  .headshot {
    position: absolute;
    left: 120px;
    bottom: 38px;
    width: 240px;
    height: 200px;
    background: linear-gradient(180deg, var(--photo-top), var(--photo-bottom));
  }
  .rule-top {
    position: absolute;
    right: 40px;
    top: 196px;
    width: 240px;
    height: 2px;
    background: var(--olive);
  }
  .rule-bottom {
    position: absolute;
    left: 120px;
    bottom: 36px;
    width: 340px;
    height: 2px;
    background: var(--maroon);
  }
  .person {
    position: absolute;
    right: 90px;
    top: 212px;
    text-align: left;
  }
  .person-name { font-weight: 900; font-size: 24px; color: var(--olive); }
  .person-role { font-size: 15px; color: var(--maroon); margin-top: 2px; }
</style>
</head>
<body>
  <section class="card card-back">
    <div class="wordmark">Brightwell Painting</div>
    <ul class="contact-list">
      <li>
        <svg viewBox="0 0 12 12"><path d="M2 1.5h2.2l1 2.5-1.4 1a6 6 0 0 0 3.2 3.2l1-1.4 2.5 1v2.2A1 1 0 0 1 9.5 11 8.5 8.5 0 0 1 1 2.5a1 1 0 0 1 1-1z"/></svg>
        555-014-2876
      </li>
      <li>
        <svg viewBox="0 0 12 12"><rect x="1" y="2.5" width="10" height="7"/><path d="M1 2.5l5 4 5-4"/></svg>
        Mark.Brightwell@mailbox.com
      </li>
      <li>
        <svg viewBox="0 0 12 12"><circle cx="6" cy="6" r="5"/><ellipse cx="6" cy="6" rx="2.2" ry="5"/><path d="M1 6h10"/></svg>
        www.BrightwellPainting.com
      </li>
    </ul>
  </section>

  <section class="card card-front">
    <div class="wordmark">Brightwell Painting</div>
    <div class="headshot" role="img" aria-label="Headshot of the card holder, smiling, in a light shirt and striped tie"></div>
    <div class="rule-top"></div>
    <div class="person">
      <div class="person-name">Mark Ellison</div>
      <div class="person-role">Quality Manager</div>
    </div>
    <div class="rule-bottom"></div>
  </section>
</body>
</html>
```